Web Design Project

We are looking for a new site design for the KELVO Canada. The current site can be found at
http://www.kelvocanada.example/
The URL is provided for reference. We want a completely different look and layout which is shown in the specifications document.
As part of the design, we want a home page, and inside page.
The design you provide will be implemented in Joomla. The design winner will only need to provide the PSD. We anticipate creating the template coding in-house.
However, if you have experience creating Joomla templates, please let us know as we may ask you to bid separately to do that phase of the project.
We've provided a specifications document which includes wireframes of the home page, and inside page. We've also included a logo file.
For the header at the top, as indicated in the specs document, we want to keep the same overall treatment to every page. We want a graphic treatment with the logo for the header area. In this manner, the design will be flexiable and can be used for future years.
For the home page, we've indicated that we'd like to have a slider implemented within the design.
The wireframe is provided to illustrate the placement of content and menu items. The exact dimensions of each component can be revised as you see fit. We are also flexiable if you feel we have missed items.

```html
<!DOCTYPE html>
<html lang="en">
<head>
<meta charset="utf-8">
<title>KELVO Canada Conference</title>
<link rel="stylesheet" href="https://fonts.googleapis.com/css2?family=Open+Sans:wght@400;600;700&family=Oswald:wght@500;600&display=swap">
<style>
:root{
  --blue:#2b4488;
  --blue-dark:#1f3370;
  --blue-light:#4d68b0;
  --red:#e0262b;
  --red-dark:#b51b1f;
  --page:#ececec;
  --panel:#f7f7f7;
  --text:#222;
  --muted:#555;
  --footer:#5a5a5a;
}
*{box-sizing:border-box;margin:0;padding:0}
html,body{width:1200px;height:1188px;overflow:hidden}
body{position:relative;background:var(--page);font-family:Arial,Helvetica,sans-serif;color:var(--text)}
.abs{position:absolute}
.header{left:0;top:0;width:1200px;height:126px;background:linear-gradient(#fff,#ececec);border-top:3px solid var(--blue);border-bottom:2px solid #666}
.brand{left:118px;top:44px;font:700 32px 'Open Sans',sans-serif;color:var(--blue);letter-spacing:1px;line-height:1}
.top-tab{left:790px;top:0;width:307px;height:32px;background:var(--red);border-radius:0 0 14px 14px;color:#fff;font:500 14px 'Oswald',sans-serif;text-align:center;line-height:32px;letter-spacing:.3px}
.follow{left:922px;top:84px;font:600 18px 'Oswald',sans-serif;color:#333;line-height:26px}
.follow-icon{top:87px;width:22px;height:22px;border-radius:3px;background:#444}
.banner{left:102px;top:134px;width:988px;height:314px;border:5px solid var(--blue);border-radius:6px;background:linear-gradient(100deg,#e9e4df 0%,#f4f6fb 30%,#cfe2f5 55%,#5b9ee0 75%,#e8f1fb 100%)}
.nav{left:102px;top:462px;width:996px;height:42px;border-radius:12px;background:linear-gradient(#4f6fb5,var(--blue) 55%,var(--blue-dark));display:flex;font:600 12px 'Open Sans',sans-serif;color:#fff}
.nav span{display:flex;align-items:center;justify-content:center;border-right:1px solid #22376f;height:100%}
.nav .active{background:linear-gradient(#ef4044,var(--red));position:relative}
.nav .active:after{content:"";position:absolute;bottom:-7px;left:50%;margin-left:-6px;border:6px solid transparent;border-top:6px solid var(--red);border-bottom:0;height:0}
.panel{background:linear-gradient(#fbfbfb,var(--panel));border-radius:12px;box-shadow:0 0 4px rgba(0,0,0,.15)}
.ribbon{left:93px;width:227px;height:34px;background:var(--red);clip-path:polygon(0 0,100% 0,88% 100%,0 100%);color:#fff;font:600 17px 'Open Sans',sans-serif;padding-left:30px;line-height:34px}
.ribbon-fold{left:93px;width:10px;height:9px;background:var(--red-dark);clip-path:polygon(0 0,100% 0,100% 100%)}
.badge{width:56px;height:56px;border-radius:50%;background:#d8dbe3}
.field{left:111px;width:215px;height:34px;border-radius:17px;background:#fff;border:1px solid #ddd;box-shadow:inset 0 2px 3px rgba(0,0,0,.08);font-size:12px;color:#666;padding:11px 0 0 12px;line-height:1}
.btn{left:244px;top:922px;width:80px;height:25px;border-radius:10px;background:var(--red);color:#fff;font:600 13px 'Open Sans',sans-serif;text-align:center;line-height:25px}
.social{top:1038px;width:27px;height:27px;border-radius:3px}
.welcome-title{left:406px;top:561px;font:600 20px 'Open Sans',sans-serif;color:#333;line-height:26px}
.welcome-title b{color:var(--blue);font-weight:600}
.rss{left:358px;top:553px;width:42px;height:42px;border-radius:6px;background:linear-gradient(#f8a03a,#e3701a);border:3px solid #eee;box-shadow:0 1px 3px rgba(0,0,0,.3)}
.dots{border-top:1px dotted #999}
.body-copy{left:371px;top:622px;width:435px;font-size:12.3px;line-height:18px;text-align:justify;color:#222}
.body-copy p{margin-bottom:18px}
.body-copy a{color:var(--red);text-decoration:none}
.popular-title{left:875px;top:566px;font:600 20px 'Open Sans',sans-serif;color:#333}
.popular-title b{color:var(--blue);font-weight:600}
.entry{left:841px;width:229px;font:11px/18px 'Open Sans',sans-serif;color:#555;text-align:justify}
.entry strong{display:block;color:var(--blue);font-weight:700;line-height:14px}
.regions-title{left:384px;top:893px;font:600 23px 'Open Sans',sans-serif;color:#333}
.region{top:944px}
.region h3{font:600 15px 'Open Sans',sans-serif;color:var(--red);margin-bottom:10px}
.region li{list-style:none;font-size:12.5px;line-height:24px;padding-left:16px;position:relative}
.region li:before{content:"";position:absolute;left:2px;top:8px;border:4px solid transparent;border-left:5px solid var(--red-dark);border-right:0}
.footer{left:0;top:1120px;width:1200px;height:68px;background:linear-gradient(#6e6e6e,#4a4a4a);color:#eee;font:12.5px 'Open Sans',sans-serif;text-align:center}
.footer .links{margin-top:16px}
.footer .links i{font-style:normal;margin:0 8px}
.footer .copy{margin-top:10px;font-size:12.5px}
</style>
</head>
<body>
<header class="abs header">
  <div class="abs brand">KELVO</div>
  <div class="abs top-tab">Login &nbsp;/&nbsp; Register Now &nbsp;/&nbsp; KELVO International</div>
  <div class="abs follow">Follow Us :</div>
  <div class="abs follow-icon" style="left:1010px"></div>
  <div class="abs follow-icon" style="left:1036px"></div>
  <div class="abs follow-icon" style="left:1062px"></div>
</header>

<div class="abs banner" role="img" aria-label="Slider photo: businesswoman on the phone beside a blue world map with business people standing on it"></div>

<nav class="abs nav">
  <span style="width:90px;padding-left:20px">Home</span>
  <span style="width:136px;padding-left:20px">Boards</span>
  <span class="active" style="width:118px">Chapters</span>
  <span style="width:152px">Member Space</span>
  <span style="width:213px">Resources &amp; Knowledge</span>
  <span style="width:151px">Sponsorship</span>
  <span style="width:106px;border:0">Exhibit</span>
</nav>

<aside>
  <div class="abs panel" style="left:104px;top:552px;width:237px;height:541px"></div>
  <div class="abs ribbon" style="top:564px">Sponsers</div><div class="abs ribbon-fold" style="top:598px"></div>
  <div class="abs badge" style="left:122px;top:618px"></div>
  <div class="abs badge" style="left:230px;top:614px;background:#d5dbec"></div>
  <div class="abs badge" style="left:122px;top:694px;border-radius:8px"></div>
  <div class="abs badge" style="left:230px;top:692px;border-radius:8px;background:#d5dbec"></div>

  <div class="abs ribbon" style="top:784px">Member Login</div><div class="abs ribbon-fold" style="top:818px"></div>
  <div class="abs field" style="top:838px">Username</div>
  <div class="abs field" style="top:879px">Password</div>
  <div class="abs btn">Login</div>

  <div class="abs ribbon" style="top:974px">Stay Connected</div><div class="abs ribbon-fold" style="top:1008px"></div>
  <div class="abs social" style="left:133px;background:#3b5ca8"></div>
  <div class="abs social" style="left:180px;background:#35b5e5"></div>
  <div class="abs social" style="left:228px;background:#1576b6"></div>
  <div class="abs social" style="left:277px;background:#f08a1e"></div>
</aside>

<main>
  <div class="abs rss"></div>
  <h1 class="abs welcome-title"><b>Welcome to</b> KELVO Canada Conference</h1>
  <div class="abs dots" style="left:402px;top:592px;width:390px"></div>
  <div class="abs body-copy">
    <p>It is a long established fact that a reader will be distracted by the readable content of a page when looking at its layout. The point of using Lorem Ipsum is that it has a more-or-less normal distribution of letters, as opposed to using 'Content here, content here', making it look like readable English.</p>
    <p>Many desktop publishing packages and web page editors now use Lorem Ipsum as their default model text, and a search for 'lorem ipsum' will uncover many web sites still in their infancy.Various versions have evolved over the years, sometimes by accident, sometimes on purpose (injected humour and the like).readable content of a page when looking at its layout. The point of using Lorem Ipsum sometimes on purpose (injected humour and the like). readable content of a page when looking at its layout. The point sometimes on purpose (injected humour and the like). <a href="#">[view more]</a></p>
  </div>

  <section>
    <div class="abs panel" style="left:825px;top:552px;width:263px;height:314px"></div>
    <svg class="abs" style="left:835px;top:562px" width="34" height="32" viewBox="0 0 34 32"><ellipse cx="17" cy="26" rx="15" ry="5" fill="#4aa22a"/><circle cx="14" cy="14" r="7" fill="#7cc241"/><circle cx="24" cy="10" r="5" fill="#e0262b"/></svg>
    <h2 class="abs popular-title"><b>Popular</b> Entries</h2>
    <div class="abs entry" style="top:607px"><strong>Weekly Picks: InkLane s</strong>from Around the Web Favorite Links from Around the Web April 2nd-6th</div>
    <div class="abs dots" style="left:841px;top:668px;width:231px"></div>
    <div class="abs entry" style="top:673px"><strong>Weekly Picks: InkLane s</strong>from Around the Web Favorite Links from Around the Web April 2nd-6th</div>
    <div class="abs dots" style="left:841px;top:734px;width:231px"></div>
    <div class="abs entry" style="top:739px"><strong>Weekly Picks: InkLane s</strong>from Around the Web Favorite Links from Around the Web April 2nd-6th</div>
    <div class="abs dots" style="left:841px;top:800px;width:231px"></div>
    <div class="abs entry" style="top:805px"><strong>Weekly Picks: InkLane s</strong>from Around the Web Favorite Links from Around the Web April 2nd-6th</div>
  </section>

  <section>
    <div class="abs panel" style="left:357px;top:877px;width:731px;height:216px"></div>
    <h2 class="abs regions-title">Regions</h2>
    <div class="abs region" style="left:388px"><h3>Mountain Pacific</h3><ul><li>Vancouver Island</li><li>Vancouver</li><li>Calgary</li></ul></div>
    <div class="abs region" style="left:567px"><h3>Western</h3><ul><li>Edmonton</li><li>Saskatchewan</li><li>Winnipeg</li></ul></div>
    <div class="abs region" style="left:729px"><h3>Central</h3><ul><li>National Capital-Ottawa</li><li>Southwestern Ontario</li><li>Montreal</li><li>Toronto</li></ul></div>
    <div class="abs region" style="left:923px"><h3>Atlantic</h3><ul><li>Nova Scotia</li><li>Terra-Nova, St. John's</li><li>Prince Edward Island</li><li>Atlantic, St. John's</li></ul></div>
  </section>
</main>

<footer class="abs footer">
  <div class="links">Home<i>|</i>About<i>|</i>Board<i>|</i>Chapters<i>|</i>Member Space<i>|</i>Resources &amp; Knowledge<i>|</i>Sponsorship<i>|</i>Exhibit<i>|</i>Member Login<i>|</i>Contact Us</div>
  <div class="copy">Copyright @ KELVO International.com &nbsp;. All Right Reserved</div>
</footer>
</body>
</html>
```